Lakemond Drywork Business Card Design

Professional and clean design. The design colors should flow with the logo. Two-sided card with the website on the back which is:

www.LakemondDrywork.example.

"Specializing in Water Damage Restoration"

On the front I need the name, email, phone, and logo.

Name: Darnell Quimby
Email: Darnell@LakemondDrywork.example
Phone: 555-018-2364 for now

I only have the Preview and Thumbnail right now but should have the source files uploaded within a day or two.

Target Market(s)

Flood victims, home owners with water damage from busted pipes etc...

Industry/Entity Type

Business

Contact Information for Business Card

Name: Darnell Quimby

Font styles to use
Serif
Sans Serif

Requirements
Must have
• Business Card Details Info

```html
<!DOCTYPE html>
<html lang="en">
<head>
<meta charset="utf-8">
<title>Lakemond Drywork – Business Card</title>
<link rel="stylesheet" href="https://fonts.googleapis.com/css2?family=Cinzel:wght@600&family=Tinos:wght@400;700&display=swap">
<style>
  :root {
    --stage: #2b2b2d;
    --card-dark: #0d0d0e;
    --card-dark-edge: #1c1c1e;
    --card-light: #ffffff;
    --brand-blue: #3aa3e3;
    --brand-blue-soft: rgba(58, 163, 227, 0.08);
    --ghost-dark: rgba(255, 255, 255, 0.05);
    --ink-light: #f2f2f2;
    --ink-dark: #3a3a3a;
    --divider: #8a8a8a;
  }
  * { box-sizing: border-box; margin: 0; padding: 0; }
  html, body {
    width: 1200px; height: 913px; overflow: hidden;
    background: var(--stage);
  }
  .stage {
    width: 1200px; height: 913px;
    display: flex; flex-direction: column; align-items: center; justify-content: center;
    gap: 56px;
  }
  .card {
    position: relative;
    width: 630px; height: 360px;
    border-radius: 26px;
    overflow: hidden;
    box-shadow: 0 18px 40px rgba(0, 0, 0, 0.45);
  }
  .card--back {
    background: linear-gradient(135deg, var(--card-dark-edge) 0%, var(--card-dark) 55%);
  }
  .card--front { background: var(--card-light); }

  .ghost-circle {
    position: absolute; border-radius: 50%;
    width: 270px; height: 270px; top: -70px; right: 70px;
  }
  .card--back .ghost-circle { background: var(--ghost-dark); }
  .card--front .ghost-circle { background: var(--brand-blue-soft); }

  .brand {
    position: absolute;
    display: flex; align-items: center; gap: 16px;
  }
  .brand__mark {
    width: 58px; height: 58px; border-radius: 50%;
    background: var(--brand-blue); flex: none;
  }
  .brand__name {
    font-family: "Cinzel", serif; font-weight: 600;
    font-size: 34px; line-height: 1.05; letter-spacing: 1px;
    color: var(--brand-blue); text-transform: uppercase;
  }
  .card--back .brand { left: 60px; top: 140px; }
  .card--front .brand { left: 110px; top: 92px; }

  .back-lines {
    position: absolute; right: 44px; bottom: 48px;
    text-align: right; color: var(--ink-light);
    font-family: "Tinos", serif;
  }
  .back-lines__web { font-size: 15px; margin-bottom: 6px; }
  .back-lines__tagline { font-size: 19px; font-weight: 700; }

  .front-details {
    position: absolute; left: 60px; right: 40px; bottom: 58px;
    display: flex; align-items: center; gap: 22px;
    font-family: "Tinos", serif;
  }
  .person-name {
    font-weight: 700; font-size: 21px; color: var(--brand-blue);
    text-transform: uppercase; letter-spacing: 0.5px; white-space: nowrap;
  }
  .divider { width: 1px; height: 44px; background: var(--divider); }
  .contact-list { list-style: none; color: var(--ink-dark); font-size: 15px; }
  .contact-list li { display: flex; align-items: center; gap: 8px; line-height: 1.6; }
  .contact-list svg { width: 13px; height: 13px; fill: var(--brand-blue); flex: none; }
</style>
</head>
<body>
<main class="stage">
  <section class="card card--back" aria-label="Card back">
    <div class="ghost-circle"></div>
    <div class="brand">
      <span class="brand__mark"></span>
      <span class="brand__name">Lakemond<br>Drywork</span>
    </div>
    <div class="back-lines">
      <p class="back-lines__web">www.LakemondDrywork.example</p>
      <p class="back-lines__tagline">Specializing in Water Damage Restoration</p>
    </div>
  </section>

  <section class="card card--front" aria-label="Card front">
    <div class="ghost-circle"></div>
    <div class="brand">
      <span class="brand__mark"></span>
      <span class="brand__name">Lakemond<br>Drywork</span>
    </div>
    <div class="front-details">
      <p class="person-name">Darnell Quimby</p>
      <span class="divider"></span>
      <ul class="contact-list">
        <li>
          <svg viewBox="0 0 24 24" aria-hidden="true"><path d="M6.6 10.8a15.1 15.1 0 0 0 6.6 6.6l2.2-2.2a1 1 0 0 1 1-.25 11.4 11.4 0 0 0 3.6.57 1 1 0 0 1 1 1V20a1 1 0 0 1-1 1A17 17 0 0 1 3 4a1 1 0 0 1 1-1h3.5a1 1 0 0 1 1 1c0 1.25.2 2.45.57 3.57a1 1 0 0 1-.25 1z"/></svg>
          555-018-2364
        </li>
        <li>
          <svg viewBox="0 0 24 24" aria-hidden="true"><path d="M2 5h20v14H2zm2 2v.5l8 5 8-5V7zm0 2.9V17h16V9.9l-8 5z"/></svg>
          Darnell@LakemondDrywork.example
        </li>
      </ul>
    </div>
  </section>
</main>
</body>
</html>
```